Restaurant business revamping our look and need a new modern menu

We need a new menu that is appealing, similar to the look of our new logo while also keeping our "cozy, clean, Midland staple" feel and gets peoples eyes on the high price items and top sellers. We are a deli that's been around since 1984, with lots of Burgers, Curly Fries, Reuben, Salads, etc.
Once we like that menu, we will need our pizza specials menu updated to look similar.

Please refer to our website for menu word format www.haldensofbrookvale.com

Target Market(s)

Every day Midlanders

Industry/Entity Type

Restaurant

Requirements
Must have
• Current menu is a trifold - not a must have but nice layout

```html
<!DOCTYPE html>
<html lang="en">
<head>
<meta charset="utf-8">
<title>Halden's Menu</title>
<link rel="stylesheet" href="https://fonts.googleapis.com/css2?family=Questrial&family=Mulish:wght@300;400;500;700&family=Rye&family=Alegreya+Sans:wght@400;500;700&display=swap">
<style>
:root{
  --page:#2b2b2b;
  --cream:#fdfcee;
  --ink:#161616;
}
*{margin:0;padding:0;box-sizing:border-box}
html,body{width:689px;height:1200px;overflow:hidden;background:var(--page)}
body{position:relative;font-family:"Mulish",sans-serif;font-weight:300;color:var(--ink)}
.panel{position:absolute;width:230px;height:506px;background:var(--cream)}
.frame{position:absolute;left:0;top:0;width:230px;height:506px}
.ln{position:absolute;left:0;right:0;text-align:center;white-space:nowrap;line-height:10px;font-size:7px}
.sm{font-size:4.3px}
.sec-head{position:absolute;left:0;right:0;height:16px;display:flex;align-items:center;justify-content:center;gap:3px;font-family:"Questrial",sans-serif;font-weight:400;font-size:16px;line-height:16px;letter-spacing:.2px}
.sec-head::before,.sec-head::after{content:"";height:1px;width:var(--rule,36px);background:var(--ink)}
.brand{font-family:"Mulish",sans-serif;font-weight:700;text-align:center;position:absolute;left:0;right:0}

/* cover */
.cover-intro{position:absolute;left:36px;width:158px;top:192px;text-align:center;font-size:6.8px;line-height:8.9px;color:var(--ink)}
.cover-intro b{font-weight:700}
.menu-word{position:absolute;left:0;right:0;top:318px;text-align:center;font-family:"Rye",serif;font-size:44px;line-height:44px;letter-spacing:1px}
.menu-rule{position:absolute;left:30px;width:170px;height:1px;background:var(--ink)}
.contact{position:absolute;left:0;right:0;text-align:center;font-size:10.5px;line-height:14px;display:flex;justify-content:center;align-items:center;gap:2px}
.contact .icon{width:8px;height:8px}
.web{--rule:32px;font-family:"Mulish",sans-serif;font-size:6.4px;height:8px;gap:6px}

/* drinks */
.drinks-list{font-family:"Mulish",sans-serif;font-size:6.8px}
.col{position:absolute;width:98px;font-family:"Alegreya Sans",sans-serif;font-size:6px;line-height:7.3px}
.col p{margin-bottom:7.3px}
.col .cap{font-weight:500;text-transform:uppercase}
.bake{position:absolute;left:20px;right:20px;text-align:center;font-family:"Alegreya Sans",sans-serif;font-size:5.6px;line-height:7px}
.bake b{font-weight:700}

/* pizzas */
.specials-tag{--rule:24px;font-family:"Mulish",sans-serif;font-size:4px;height:6px;font-weight:400;letter-spacing:.3px}
.pizza-intro{position:absolute;left:50px;width:130px;text-align:center;font-size:4.3px;line-height:6.4px}
.pizza-intro b{font-weight:700}
.pizza-list{position:absolute;left:52px;width:126px;top:133px;text-align:center;font-family:"Mulish",sans-serif;font-weight:300;font-size:4.4px;line-height:7px}
.pizza-list h3{font-weight:700;font-size:4.6px}
.pizza-list p{margin-bottom:7.4px}
</style>
</head>
<body>

<svg width="0" height="0" style="position:absolute" aria-hidden="true">
  <defs>
    <g id="menu-frame" fill="none" stroke="#161616" stroke-width=".9">
      <path d="M10,38 Q20,38 20,28 L82,28 Q88,28 88,22 Q88,18 94,18 L136,18 Q142,18 142,22 Q142,28 148,28 L210,28 Q210,38 220,38 L220,468 Q210,468 210,478 L148,478 Q142,478 142,484 Q142,488 136,488 L94,488 Q88,488 88,484 Q88,478 82,478 L20,478 Q20,468 10,468 Z"/>
      <path d="M13,41 Q23,41 23,31 L84,31 Q91,31 91,25 Q91,21 96,21 L134,21 Q139,21 139,25 Q139,31 146,31 L207,31 Q207,41 217,41 L217,465 Q207,465 207,475 L146,475 Q139,475 139,481 Q139,485 134,485 L96,485 Q91,485 91,481 Q91,475 84,475 L23,475 Q23,465 13,465 Z"/>
      <g fill="#161616" stroke="none">
        <circle cx="13" cy="30" r="1.8"/><circle cx="217" cy="30" r="1.8"/>
        <circle cx="13" cy="476" r="1.8"/><circle cx="217" cy="476" r="1.8"/>
      </g>
    </g>
  </defs>
</svg>

<!-- Cover -->
<section class="panel cover" style="left:91px;top:75px">
  <svg class="frame" viewBox="0 0 230 506"><use href="#menu-frame"/></svg>
  <div class="brand" style="top:82px;font-size:30px;line-height:34px">Halden's</div>
  <p class="cover-intro">Only the finest ingredients, the choicest cuts of meats and the freshest produce will be good enough<br>for our customers. Our beef products are from the round cut (leanest possible) therefore the most “heart healthy”. Our turkey is smoked breast 98% fat free. We make our salads fresh from scratch. We want you to know these facts so you will understand why we feel we are unique in the Permian Basin. To state our philosophy in a single word, it is <b>“QUALITY”.</b></p>
  <div class="menu-rule" style="top:315px"></div>
  <div class="menu-word">MENU</div>
  <div class="menu-rule" style="top:366px"></div>
  <div class="contact" style="top:383px">1480 W. Larkin</div>
  <div class="contact" style="top:396px">Brookvale, Texas 79614</div>
  <div class="contact" style="top:410px">
    <svg class="icon" viewBox="0 0 10 10" aria-hidden="true"><circle cx="5" cy="5" r="5" fill="#161616"/><path d="M3.2 2.4l1 1-.5.8c.4.8 1 1.4 1.8 1.8l.8-.5 1 1-.6.9C4.8 7.2 2.8 5.2 2.4 3.1z" fill="#fdfcee"/></svg>(555) 014-2277
  </div>
  <div class="contact" style="top:424px">
    <svg class="icon" viewBox="0 0 10 10" aria-hidden="true"><circle cx="5" cy="5" r="5" fill="#161616"/></svg>@haldens_deli
  </div>
  <div class="sec-head web" style="top:460px">www.haldensofbrookvale.com</div>
</section>

<!-- Soups, appetizers, kids, desserts -->
<section class="panel food" style="left:369px;top:75px">
  <svg class="frame" viewBox="0 0 230 506"><use href="#menu-frame"/></svg>
  <h2 class="sec-head" style="top:38px;--rule:34px">SOUPS</h2>
  <div class="ln" style="top:57px;left:46px;text-align:left">Cream of Broccoli</div>
  <div class="ln" style="top:57px;left:125px;text-align:left">Potato with Bacon</div>
  <div class="ln" style="top:68px;left:46px;text-align:left">Wisconsin Cheese</div>
  <div class="ln" style="top:68px;left:125px;text-align:left">Chicken Noodle</div>
  <div class="ln" style="top:79px">Tomato Basil</div>
  <div class="ln sm" style="top:87px">Cup&ensp;4.25&emsp;&emsp;&emsp;Bowl&ensp;5.25</div>
  <div class="ln" style="top:101px">Seafood Gumbo</div>
  <div class="ln sm" style="top:109px">Cup&ensp;5.50&emsp;&emsp;&emsp;Bow&ensp;6.50</div>

  <h2 class="sec-head" style="top:133px;--rule:38px">APPETIZERS</h2>
  <div class="ln" style="top:155px">Breaded Cheese Sticks&emsp;&ensp;10.50</div>
  <div class="ln" style="top:164px">“Signature” marinara sauce +1.25</div>
  <div class="ln" style="top:180px">Zucchini Chips&emsp;&ensp;9.95</div>
  <div class="ln" style="top:189px">“Signature” marinara sauce +1.25</div>
  <div class="ln" style="top:203px">Onion Rings&ensp;9.95</div>
  <div class="ln" style="top:212px">Chips &amp; Queso&emsp;&ensp;6.25</div>
  <div class="ln" style="top:221px">Potachos&emsp;10.05</div>
  <div class="ln" style="top:230px">with blackened or grilled chicken 12.25</div>

  <h2 class="sec-head" style="top:254px;--rule:42px">KIDS</h2>
  <div class="ln" style="top:273px">Mac and Cheese</div>
  <div class="ln sm" style="top:282px">Cup&ensp;3&emsp;&emsp;Bowl&ensp;4.50</div>
  <div class="ln" style="top:292px">All Beef Hot Dog&ensp;&ensp;6.25</div>
  <div class="ln" style="top:302px">Peanut Butter &amp; Jelly with side&emsp;6.00</div>
  <div class="ln" style="top:312px">Grilled Cheese Sandwich with side&emsp;&ensp;6.25</div>
  <div class="ln" style="top:323px">Apple Juice&ensp;1.50</div>

  <h2 class="sec-head" style="top:347px;--rule:40px">DESSERTS</h2>
  <div class="ln" style="top:367px">Iced Brownies&emsp;&ensp;2.15</div>
  <div class="ln" style="top:377px">Carrot Cake&ensp;4</div>
  <div class="ln" style="top:387px">Boston Cream Pie&ensp;4</div>
  <div class="ln" style="top:397px">Key Lime Pie 6.25</div>
  <div class="ln" style="top:407px">Chocolate Mousse Cake&emsp;6.50</div>
  <div class="ln" style="top:418px">New York Colossal Cheesecake&emsp;6.25</div>
  <div class="ln" style="top:428px">The “Real Deal” Cannoli&emsp;6.50</div>
  <div class="ln" style="top:438px">Lemon Tart&ensp;.25</div>
  <div class="ln" style="top:448px">Texas Chocolate Sheet Cake&emsp;&ensp;4.50</div>
  <div class="ln" style="top:458px">Italian Cream Cake&ensp;4.50</div>
</section>

<!-- Drinks, beer & wines, take & bake -->
<section class="panel drinks" style="left:91px;top:620px">
  <svg class="frame" viewBox="0 0 230 506"><use href="#menu-frame"/></svg>
  <h2 class="sec-head" style="top:43px;--rule:44px">DRINKS</h2>
  <div class="ln drinks-list" style="top:63px">Cola, Diet Cola, Cherry Cola, Lemon-Lime Soda, Root Beer,</div>
  <div class="ln drinks-list" style="top:73px">Pepper Soda, Cream Soda, Tea, Raspberry Tea, Lemonade,</div>
  <div class="ln drinks-list" style="top:83px">Coffee (regular or decaf), Sparkling Mineral 2.49</div>
  <div class="ln drinks-list" style="top:93px">Bottled Water 1.95 Vapor Water 3.45</div>
  <div class="ln drinks-list" style="top:103px">Large Drinks 3.39</div>

  <h2 class="sec-head" style="top:126px;--rule:42px">BEER &amp; WINES</h2>
  <div class="col" style="left:30px;top:148px">
    <p class="cap">Wine List<br><span style="text-transform:none">(*Proprietor’s Choice):</span></p>
    <p>• * Willow Ridge Cab<br>Bottle 375 ml. 16<br>Glass 8.75</p>
    <p>• * Bellcrest Pinot Noir<br>Bottle 375 ml. 14<br>Glass 7.75</p>
    <p>• * Route 12 Sauvignon Blanc<br>Bottle 375 ml. 13<br>Glass 7.50</p>
    <p>• * Cedar Bluff<br>Chardonnay<br>Bottle 375 ml. 19<br>Glass 10</p>
    <p>• White Zinfandel,<br>Pinot Grigio<br>Glass 7.50</p>
    <p style="margin-bottom:2px">• Hard Seltzers 4.95</p>
    <p class="cap">Specialty Bottled<br>Beer 4.95</p>
    <p class="cap">Domestic Bottled<br>Beer 4.25</p>
  </div>
  <div class="col" style="left:132px;top:148px">
    <p><span class="cap">Specialty &amp;<br>Microbrew Draft<br>Beer</span><br>(*Proprietor’s Choice)<br>5.75</p>
    <p>• *Half &amp; Half (Kingsley Ale<br>topped with Blackwell Stout)</p>
    <p>• Tall Mesa Brewing Co.<br>Two Mile Divide<br>(American Amber)<br>Brookvale, Texas</p>
    <p>• Tall Mesa Brewing Co.<br>Dust Devil (IPA)<br>Brookvale, Texas</p>
    <p style="margin-bottom:0">• Oddfellow Brewing Co.<br>Rotating Beer<br>Brookvale, Texas<br>• Blackwell Stout<br>• Dos Rios Lager<br>• Kingsley Ale<br>• Stellan Pils<br>• Lone Gulch Bock</p>
    <p><span class="cap">&ensp;Domestic on Tap</span> 4.50<br>• Mesa Light</p>
  </div>

  <h2 class="sec-head" style="top:390px;font-size:10.5px;--rule:32px">TAKE &amp; BAKE PIZZAS</h2>
  <div class="bake" style="top:404px"><b>Halden’s Homemade Wood-Fire Brick Oven Frozen<br>Pizza Available for Purchase Any Time or Day of the Week!<br>Immediately Available Options on our Homemad Dough</b></div>
  <div class="bake" style="top:436px">Carnivore • Pepperoni • Cheese • Fig • Luigi • Veggie • Steamboat<br>Call ahead for other Halden’s Pizza Specialty Options or Build Your Own!</div>
  <div class="bake" style="top:454px">(Build your own options will be made Thursday, Friday or Saturday!)</div>
</section>

<!-- Weekend pizza specials -->
<section class="panel pizzas" style="left:369px;top:620px">
  <svg class="frame" viewBox="0 0 230 506"><use href="#menu-frame"/></svg>
  <div class="brand" style="top:38px;font-size:17px;line-height:20px">Halden's</div>
  <div class="sec-head specials-tag" style="top:60px">WEEKEND SPECIALS</div>
  <p class="pizza-intro" style="top:66px"><b>(Tuesday &amp; Friday 4 PM – 9 PM • Saturday 11 AM – 3 PM)</b><br>Traditional “Old World” Italian thin crust pizza with our homemade sauces and homemade dough aged in our cooler before becoming a pizza! Because we bake in a custom built, wood-fired brick oven at 700 – 800 degrees, some charring of the crust is normal.</p>

  <h2 class="sec-head" style="top:112px;font-size:10px;--rule:34px">SPECIALTY PIZZAS</h2>
  <div class="pizza-list">
    <h3>Cinque Formaggio</h3>
    <p>Creamy garlic white sauce with asiago, provolone, parmesan, mozzarella, ricotta, and fresh rosemary 14</p>
    <h3>Classic Margherita</h3>
    <p>Pure and Simple – Red sauce, fresh mozzarella, tomatoes, and fresh basil 14</p>
    <h3>Marlow Classic</h3>
    <p>A family take on the Classic Margherita Pizza – Red sauce, fresh mozzarella, sliced tomatoes, Italian sausage, and fresh basil 14</p>
    <h3>Carnivore</h3>
    <p>Red sauce, mozzarella, pepperoni and Italian sausage 4</p>
    <h3>Fig</h3>
    <p>Fig jam, provolone, prosciutto, fresh mozzarella, drizzled balsamic glaze reduction (try it with bleu cheese crumbles!) 16</p>
    <h3>Luigi</h3>
    <p>Red sauce, mozzarella, finely chopped ground beef, diced green peppers, drizzled serrano infused oil 14</p>
    <h3>BBQ Chicken</h3>
    <p>BBQ Sauce, mozzarella, smoked gouda, shredded chicken, purple onion, bacon, pickles, and cilantro 14</p>
    <h3>Hawaiian</h3>
    <p>Red sauce, mozzarella, provolone, Canadian bacon, fresh pineapple 14</p>
    <h3>Sweet &amp; Spicy</h3>
    <p>Red sauce, mozzarella, pepperoni, candied jalapenos, honey drizzle 14</p>
    <h3>Cheese</h3>
    <p>Red sauce, mozzarella, provolone, and cheddar! 10.50</p>
    <h3>Pepperoni</h3>
    <p>Red sauce, mozzarella, provolone, cheddar, and pepperoni 12</p>
    <h3>Cinnamon Wheel</h3>
    <p>Cinnamon buttery goodness with brown sugar, old fashioned oats and a white frosting drizzle 10</p>
  </div>
</section>

</body>
</html>
```